IT Company Business Card Rebranding

We want to modernize our business cards massively. We want to incorporate aspects of our old business card such as the white and geometric design with the blues of another icon. Existing Logo, old business card and icon are all attached.

We are a modern IT company that provides support for new and growing technologies and want our business cards to be modern yet professional.
Updates

Note: Do not use file ICON.png in design. This is just a design we like Added Wednesday, March 9, 2016

Industry/Entity Type

Information Technology

Contact Information for Business Card

Roughly 43 : 26 or 1075 x 650 px

Font styles to use
Serif

Colors
0492cd
3276b5
33a6d7
86cfc6
cfeae6
cee9f5
ffffff

Requirements
Must have
• Modern yet professional
Nice to have
• We would like to incorporate the blues of our existing logo and of the icon provided. Really like the design of the icon.
Should not have
• Too Decorative. Just simple and professional.
• Not have the circle icon, as it is a copyrighted icon, I just like the colors and the geometric design

```html
<!DOCTYPE html>
<html lang="en">
<head>
<meta charset="utf-8">
<title>Northwave IT – Business Card</title>
<link rel="stylesheet" href="https://fonts.googleapis.com/css2?family=Tinos:wght@400;700&display=swap">
<style>
  :root {
    --page: #eef0f2;
    --card: #ffffff;
    --ink-blue: #2b3fb0;
    --ink-grey: #8a8d92;
    --rule: #b9bcc0;
    --blue-deep: #3240a8;
    --blue-mid: #3276b5;
    --blue-bright: #33a6d7;
    --blue-sky: #0492cd;
  }
  * { margin: 0; padding: 0; box-sizing: border-box; }
  html, body {
    width: 1200px; height: 1022px; overflow: hidden;
    background: var(--page);
  }
  .card {
    position: absolute; left: 100px; top: 208px;
    width: 1000px; height: 605px;
    background: var(--card);
    border-radius: 22px;
    overflow: hidden;
    box-shadow: 0 10px 30px rgba(0,0,0,.12);
    font-family: "Tinos", "Times New Roman", serif;
  }
  .geo-band {
    position: absolute; left: 0; bottom: 0;
    width: 560px; height: 260px;
  }
  .brand {
    position: absolute; left: 430px; top: 120px;
    display: flex; align-items: center; gap: 22px;
  }
  .brand-dot {
    width: 64px; height: 64px; border-radius: 50%;
    background: var(--blue-mid);
  }
  .brand-name {
    font-size: 40px; font-weight: 400; letter-spacing: 10px;
    color: var(--ink-grey);
  }
  .divider {
    position: absolute; left: 60px; top: 300px;
    width: 600px; height: 2px; background: var(--rule);
  }
  .contact {
    position: absolute; right: 50px; top: 262px;
    text-align: right; color: var(--ink-blue);
  }
  .contact-name {
    font-size: 40px; font-weight: 700; letter-spacing: 1px;
    line-height: 1;
    padding-bottom: 4px;
    border-bottom: 2px solid var(--ink-blue);
    display: inline-block;
  }
  .contact-role {
    font-size: 21px; color: var(--ink-grey); letter-spacing: 1px;
    margin-top: 6px; margin-bottom: 14px;
  }
  .contact-line {
    font-size: 26px; line-height: 36px;
    display: flex; justify-content: flex-end; align-items: center; gap: 10px;
  }
  .contact-line svg { width: 16px; height: 16px; flex: none; }
  .contact-line .spacer { width: 16px; }
</style>
</head>
<body>
  <div class="card">
    <svg class="geo-band" viewBox="0 0 560 260" role="img" aria-label="Geometric pattern of blue triangles along the lower corner">
      <defs>
        <linearGradient id="geoFill" x1="0" y1="1" x2="1" y2="0">
          <stop offset="0" stop-color="#3240a8"/>
          <stop offset="0.5" stop-color="#3276b5"/>
          <stop offset="1" stop-color="#33a6d7"/>
        </linearGradient>
      </defs>
      <polygon points="0,260 0,130 230,110 560,0 560,260" fill="url(#geoFill)"/>
    </svg>

    <div class="brand">
      <span class="brand-dot"></span>
      <span class="brand-name">NORTHWAVE IT</span>
    </div>

    <div class="divider"></div>

    <div class="contact">
      <div class="contact-name">MILO</div>
      <div class="contact-role">TECHNICAL SERVICES</div>
      <div class="contact-line">Roughly 43 :<span class="spacer"></span></div>
      <div class="contact-line">26 or 1075 x 650 px<span class="spacer"></span></div>
      <div class="contact-line">+330 5550-1234
        <svg viewBox="0 0 16 16" aria-hidden="true"><path d="M4 1l3 3-2 2c1 2 3 4 5 5l2-2 3 3-2 3C7 15 1 9 1 3z" fill="none" stroke="#8a8d92" stroke-width="1.3"/></svg>
      </div>
      <div class="contact-line">hello@brightdesk.net
        <svg viewBox="0 0 16 16" aria-hidden="true"><rect x="1.5" y="3.5" width="13" height="9" fill="none" stroke="#8a8d92" stroke-width="1.3"/><path d="M1.5 3.5l6.5 5 6.5-5" fill="none" stroke="#8a8d92" stroke-width="1.3"/></svg>
      </div>
      <div class="contact-line">www.brightdesk.net
        <svg viewBox="0 0 16 16" aria-hidden="true"><circle cx="8" cy="8" r="6.5" fill="none" stroke="#8a8d92" stroke-width="1.3"/><path d="M1.5 8h13M8 1.5c-3 3.5-3 9.5 0 13M8 1.5c3 3.5 3 9.5 0 13" fill="none" stroke="#8a8d92" stroke-width="1.1"/></svg>
      </div>
    </div>
  </div>
</body>
</html>
```